Under 13 cricket camp

This is a under 13 cricket camp which is sponsored yearly since 1996
"Home of Tod Veleski U-13 Cricket Cricket Camp"

1. Look at cricket poster 1....logo in the center with batsman and bowler on the sides.

```html
<!DOCTYPE html>
<html lang="en">
<head>
<meta charset="utf-8">
<title>Tod Veleski U-13 Cricket Camp</title>
<link rel="stylesheet" href="https://fonts.googleapis.com/css2?family=Montserrat:wght@600;700;800&family=Oswald:wght@500&display=swap">
<style>
  :root {
    --page: #e4e4e4;
    --paper: #ffffff;
    --brand-blue: #1660a8;
    --brand-red: #8e1a1f;
    --ink: #1b1b2a;
    --sky-light: #d6eefa;
  }
  * { margin: 0; padding: 0; box-sizing: border-box; }
  html, body { width: 1200px; height: 1200px; overflow: hidden; background: var(--page); }
  .banner {
    position: absolute; left: 30px; top: 329px;
    width: 1140px; height: 542px;
    background: var(--paper);
    font-family: "Montserrat", sans-serif;
    overflow: hidden;
  }
  .banner-art { position: absolute; inset: 0; width: 100%; height: 100%; }
  .sponsor-name {
    position: absolute; left: 110px; top: 150px;
    display: flex; align-items: center; gap: 12px;
    font-weight: 600; font-size: 28px; color: var(--ink);
  }
  .sponsor-dot { width: 22px; height: 22px; border-radius: 50%; background: var(--brand-blue); }
  .camp-home {
    position: absolute; left: 51px; top: 222px;
    font-weight: 700; font-size: 33px; color: var(--brand-red); white-space: nowrap;
  }
  .age-group {
    position: absolute; left: 46px; top: 262px;
    font-weight: 800; font-size: 168px; line-height: 1;
    letter-spacing: -0.07em; color: var(--brand-blue);
  }
  .camp-label {
    position: absolute; left: 331px; top: 307px; width: 199px; height: 83px;
    background: var(--brand-red); color: var(--paper);
    font-weight: 600; font-size: 37px; line-height: 1;
    padding: 5px 0 0 8px;
  }
  .web-address {
    position: absolute; left: 41px; top: 408px; width: 503px; height: 49px;
    border: 3px solid var(--brand-blue);
    display: flex; align-items: center; justify-content: center;
    font-weight: 700; font-size: 24px; color: var(--brand-blue);
  }
  .web-address .domain { color: var(--brand-red); }
  .tagline-band {
    position: absolute; left: 0; top: 501px; width: 100%; height: 41px;
    background: var(--brand-blue); color: var(--paper);
    display: flex; align-items: center; justify-content: center;
    font-family: "Oswald", sans-serif; font-weight: 500; font-size: 34px;
    letter-spacing: 0.2em;
  }
</style>
</head>
<body>
  <div class="banner">
    <svg class="banner-art" viewBox="0 0 1262 600" preserveAspectRatio="none">
      <defs>
        <linearGradient id="panel-sky" x1="0" y1="0" x2="0" y2="1">
          <stop offset="0" stop-color="#ffffff"/>
          <stop offset="1" stop-color="#d6eefa"/>
        </linearGradient>
        <linearGradient id="player-tones" x1="0" y1="0" x2="1" y2="1">
          <stop offset="0" stop-color="#f3a3a0"/>
          <stop offset="0.5" stop-color="#9fe3f0"/>
          <stop offset="1" stop-color="#8aa6e0"/>
        </linearGradient>
      </defs>
      <path d="M830 0 L1262 0 L1262 555 L780 555 C690 400 700 150 830 0 Z" fill="url(#panel-sky)"/>
      <path d="M780 0 C640 150 600 400 710 555" fill="none" stroke="#8e1a1f" stroke-width="12"/>
      <path d="M810 0 C680 150 650 400 760 555" fill="none" stroke="#1660a8" stroke-width="10"/>
      <rect x="760" y="35" width="480" height="520" rx="40" fill="url(#player-tones)" opacity="0.55"
            role="img" aria-label="Illustration of a young batsman playing a shot at a red cricket ball with colourful swooshes"/>
    </svg>

    <div class="sponsor-name"><span class="sponsor-dot"></span>Palm Cove Apparel</div>
    <div class="camp-home">HOME OF TOD VELESKI</div>
    <div class="age-group">U13</div>
    <div class="camp-label">CRICKET<br>CAMP</div>
    <div class="web-address">WWW.<span class="domain">PALMCOVEAPPAREL</span>.COM</div>
    <div class="tagline-band">SPONSORING YOUTH CRICKET SINCE 1996</div>
  </div>
</body>
</html>
```